Letterhead needed using basic elements of our new logo!

We have just had a new logo and business card created on Pixel Harbor and now would like a new letterhead for our company re-branding. Our logo inspires trust, professionalism and confidence and we would like to mirror that in our letterhead. We would like to use elements in our logo (as well as the logo itself, obviously), but understand with only a header and the ability to print in black and white, we are somewhat limited. We have also won the Resident's Pick Medal for best Property Management Company in our city and would like to somehow include that small banner (see uploaded file) in the letterhead, without it clashing?

Text to include:
Northmere Property Management (and logo)
C-214 Tamblyn Cres, Winnipeg, MB R2K 3P7
Ph: 204-739-8152
Fax: 1-888-376-2914
Email: customerservice@northmerepropertymanagement.example
Web: www.northmerepropertymanagement.example

Pasted below is our mission, vision and branding statements to help with the project:

Mission Statement

Provide the highest quality customer service to both property owners and tenants using innovative technology and well trained, caring staff.

Vision Statement

To redefine the way in which management is delivered to its customers, becoming the recognized leader in the property management industry.

Brand Essence

When our customers experience our product or service, it brings forth an emotion of absolute trust that we have their best interests at heart

Brand Personality

We are a company that is passionate about our customers, our company and our vision to be leaders in the field of property management. We are visionaries that aren't afraid to use cutting edge technologies to improve our products and service.

Position or Value Proposition

To whom are we speaking?
- real estate investors, including first timers that are giving us their first starter home. They are fairly naive, as they are not "big time" investors, and because they are giving us their first home (in contract to an investor buying a rental property, often sight unseen) they are more emotionally tied to their property and will require a company that inspires trust and confidence.

What is our brand promise?
- we will do our best to serve our clients, both owners and tenants, to give them prompt communication, clear, concise answers to their questions, and look after their property quickly and competently.

Why is our product different than the competition and why should our customers care?
- the current model used by most management companies employs individual portfolio managers that do things a little differently each instance, and differently than their fellow staff members. Our management product is superior because we use a combination of technology and strict procedures to ensure each client's experience is consistent, each and every time.

Industry/Entity Type

Business

Requirements
Must have
• We would like an option to be in black and white, to be able to be printed from Microsoft Word. As well, we do not want anything in a footer or any other kind of letterhead that bleeds below a header. The main use of this letterhead will be from our property management software, to be used in our form letters and other templates (sent to tenants and clients)
Should not have
• Footer or other elements where the text body would be, it will be used in a form letter

```html
<!DOCTYPE html>
<html lang="en">
<head>
<meta charset="utf-8">
<title>Northmere Property Management – Letterhead</title>
<link href="https://fonts.googleapis.com/css2?family=Roboto+Condensed:wght@400;700&display=swap" rel="stylesheet">
<style>
  :root {
    --board: #272727;
    --paper: #ffffff;
    --brand-blue: #1e8fd2;
    --ink-dark: #333336;
  }
  * { box-sizing: border-box; margin: 0; padding: 0; }
  html, body { width: 1200px; height: 933px; overflow: hidden; }
  body { background: var(--board); position: relative; font-family: "Roboto Condensed", "Arial Narrow", sans-serif; }

  .sheet {
    position: absolute;
    width: 536px;
    height: 740px;
    background: var(--paper);
  }
  .sheet--color { left: 36px; top: 89px; }
  .sheet--mono  { left: 622px; top: 90px; }

  .brand {
    position: absolute;
    left: 38px;
    top: 35px;
    display: flex;
    align-items: center;
    gap: 7px;
    color: var(--brand-blue);
    font-weight: 700;
    text-transform: uppercase;
  }
  .brand__mark {
    width: 34px;
    height: 34px;
    background: var(--brand-blue);
  }
  .brand__name { line-height: 1; }
  .brand__name-main { display: block; font-size: 22px; letter-spacing: 1.6px; }
  .brand__name-sub { display: block; font-size: 8px; letter-spacing: 2.2px; margin-top: 3px; }

  .contact {
    position: absolute;
    right: 24px;
    top: 28px;
    list-style: none;
    text-align: right;
    color: var(--brand-blue);
    font-size: 6px;
    line-height: 10px;
  }
  .contact__item { display: flex; justify-content: flex-end; align-items: center; gap: 3px; }
  .contact__item--phone { font-size: 7.4px; }
  .contact__item--small { font-weight: 700; font-size: 5.4px; }
  .contact__icon { width: 8px; height: 8px; flex: none; }

  .rule {
    position: absolute;
    left: 0;
    right: 0;
    top: 81px;
    height: 2px;
    background: var(--brand-blue);
  }
  .sheet--color .rule {
    background: linear-gradient(to right, var(--brand-blue) 0 67.3%, var(--ink-dark) 67.3% 100%);
  }
</style>
</head>
<body>

<section class="sheet sheet--color" aria-label="Letterhead, colour version">
  <div class="brand">
    <span class="brand__mark"></span>
    <span class="brand__name">
      <span class="brand__name-main">Northmere</span>
      <span class="brand__name-sub">Property Management</span>
    </span>
  </div>
  <ul class="contact">
    <li class="contact__item contact__item--phone">204-739-8152
      <svg class="contact__icon" viewBox="0 0 8 8"><circle cx="4" cy="4" r="3.5" fill="none" stroke="#333336" stroke-width=".7"/><rect x="2.8" y="2" width="2.4" height="4" rx=".5" fill="none" stroke="#333336" stroke-width=".6"/></svg></li>
    <li class="contact__item contact__item--phone">1-888-376-2914
      <svg class="contact__icon" viewBox="0 0 8 8"><circle cx="4" cy="4" r="3.5" fill="#333336"/><rect x="2.3" y="3" width="3.4" height="2.4" fill="#fff"/></svg></li>
    <li class="contact__item contact__item--small">www.northmerepropertymanagement.example
      <svg class="contact__icon" viewBox="0 0 8 8"><circle cx="4" cy="4" r="3.5" fill="#333336"/><circle cx="4" cy="4" r="1.8" fill="none" stroke="#fff" stroke-width=".6"/></svg></li>
    <li class="contact__item contact__item--small">C-214 Tamblyn Cres, Winnipeg, MB R2K 3P7
      <svg class="contact__icon" viewBox="0 0 8 8"><circle cx="4" cy="4" r="3.5" fill="none" stroke="#333336" stroke-width=".7"/><path d="M4 6.2 2.6 3.8a1.5 1.5 0 1 1 2.8 0Z" fill="none" stroke="#333336" stroke-width=".6"/></svg></li>
    <li class="contact__item contact__item--small">customerservice@northmerepropertymanagement.example
      <svg class="contact__icon" viewBox="0 0 8 8"><circle cx="4" cy="4" r="3.5" fill="#333336"/><rect x="2.2" y="2.8" width="3.6" height="2.4" fill="#fff"/></svg></li>
  </ul>
  <div class="rule"></div>
</section>

<section class="sheet sheet--mono" aria-label="Letterhead, single rule version">
  <div class="brand">
    <span class="brand__mark"></span>
    <span class="brand__name">
      <span class="brand__name-main">Northmere</span>
      <span class="brand__name-sub">Property Management</span>
    </span>
  </div>
  <ul class="contact">
    <li class="contact__item contact__item--phone">204-739-8152
      <svg class="contact__icon" viewBox="0 0 8 8"><circle cx="4" cy="4" r="3.5" fill="none" stroke="#333336" stroke-width=".7"/><rect x="2.8" y="2" width="2.4" height="4" rx=".5" fill="none" stroke="#333336" stroke-width=".6"/></svg></li>
    <li class="contact__item contact__item--phone">1-888-376-2914
      <svg class="contact__icon" viewBox="0 0 8 8"><circle cx="4" cy="4" r="3.5" fill="#333336"/><rect x="2.3" y="3" width="3.4" height="2.4" fill="#fff"/></svg></li>
    <li class="contact__item contact__item--small">www.northmerepropertymanagement.example
      <svg class="contact__icon" viewBox="0 0 8 8"><circle cx="4" cy="4" r="3.5" fill="#333336"/><circle cx="4" cy="4" r="1.8" fill="none" stroke="#fff" stroke-width=".6"/></svg></li>
    <li class="contact__item contact__item--small">C-214 Tamblyn Cres, Winnipeg, MB R2K 3P7
      <svg class="contact__icon" viewBox="0 0 8 8"><circle cx="4" cy="4" r="3.5" fill="none" stroke="#333336" stroke-width=".7"/><path d="M4 6.2 2.6 3.8a1.5 1.5 0 1 1 2.8 0Z" fill="none" stroke="#333336" stroke-width=".6"/></svg></li>
    <li class="contact__item contact__item--small">customerservice@northmerepropertymanagement.example
      <svg class="contact__icon" viewBox="0 0 8 8"><circle cx="4" cy="4" r="3.5" fill="#333336"/><rect x="2.2" y="2.8" width="3.6" height="2.4" fill="#fff"/></svg></li>
  </ul>
  <div class="rule"></div>
</section>

</body>
</html>
```